Shake your trade - Site for startup to grow

Update: To clarify I've started a few wireframes: http://snipa.ly/7kq2wRt this is by no means complete or even the layout im looking for, just some idea of the elements on the first few pages

This is for design only, I require PSDs as well high res versions of logo/other asset.

Concept

The site is place where Domain experts to identify real world problems in there respective industries that could be solved with software or hard ward products.

A similar site to this is : http://www.notionpeek.com/ which allows anyone to suggest ideas for products they want realising.

Pages needing design:

1) Login

2) Problems search: List of problems posted filterable by industry. Should contain:

- User who posted the problem (name, picture, etc)
- Title and short description of the problem space
- Current state of the project i.e. team created, just started, etc.

3) Problem details page, should contain:

- Title and large description of the problem space
- Optional image
- List of products that attempt to solve the problem (Name of product, short description, url)
- Discussion board (small forum for discussing the idea)
- List of teams started to solve the problem (show number of members and current state of the team, link to public team page)

4) Post a problem page:

- Form to create a problem containing all the things above

4) Public team page

- Shows team members (name, position, link to bio)
- List of team blog posts
- Adverts for team members, funding partners, beta testers etc

5) Private team page

- The ability to change the status of the project
- The ability to post blogs promoting there project
- The ability to advertise for additional team member, funding
partners, beta testers etc
- Private discussion board

The site will be called "www.shakeyourtrade.com" and will require a logo.

Target Market(s)

software developers, designers, entrepreneurs, VCs

Industry/Entity Type

Industry

Number of Pages Required

5+ page

Font styles to use
Serif
Sans Serif

Requirements
Must have
• PSDs + high res images
• Simple clean design see:
• - https://demo.velvotboards.com/
• - https://discuss.tamvex.org/
• - https://pixlorb.com/shots/4839201-Task-Panel/attachments/538204

```html
<!DOCTYPE html>
<html lang="en">
<head>
<meta charset="utf-8">
<title>Crux Finder — Shake your trade</title>
<link rel="stylesheet" href="https://fonts.googleapis.com/css2?family=Jost:wght@300;400;500;600;700&display=swap">
<style>
:root{
  --navy:#363d57;
  --navy-deep:#2e3550;
  --blue:#1f87e3;
  --send:#4f5f8e;
  --white:#ffffff;
  --field:#f1f2f4;
  --ink:#2d3145;
  --muted:#8d93a6;
  --accent:#1d8fd6;
  --side-top:#2a9fd8;
  --side-bottom:#1a7fc4;
  --panel:#eef2f6;
  --card:#ffffff;
  --bezel:#16181d;
  --base:#b9bcc2;
  --star:#2f6fe0;
  --tag-red:#e63b3b;
  --tag-pink:#e6288f;
}
*{box-sizing:border-box;margin:0;padding:0}
html,body{width:1200px;height:675px;overflow:hidden}
body{font-family:"Jost",sans-serif;background:var(--navy);color:var(--white)}
.canvas{position:relative;width:1200px;height:675px;overflow:hidden;background:var(--navy)}
.backdrop{position:absolute;inset:0}
.brand{position:absolute;left:94px;top:26px;display:flex;align-items:center;gap:10px}
.brand-dot{width:32px;height:32px;border-radius:50%;background:var(--white)}
.brand-name{font-weight:700;font-size:15px;line-height:17px;letter-spacing:.3px;color:var(--white)}
.nav{position:absolute;top:29px;left:922px;display:flex;gap:13px}
.nav a{display:flex;align-items:center;justify-content:center;width:86px;height:30px;border-radius:15px;font-size:12px;color:var(--white);text-decoration:none;letter-spacing:.2px}
.nav .login{border:1.5px solid #aab0c4}
.nav .signup{background:var(--navy-deep)}
.hero-title{position:absolute;left:93px;top:222px;font-size:30px;font-weight:300;letter-spacing:-1px;color:#d8dbe4;white-space:nowrap}
.hero-title strong{font-weight:500;color:var(--white)}
.hero-copy{position:absolute;left:94px;top:290px;width:440px;font-size:13px;line-height:20px;font-weight:400;color:#e9ebf1;white-space:nowrap;letter-spacing:-.2px}
.signup-form{position:absolute;left:94px;top:405px;width:358px;height:37px;display:flex;border-radius:19px;overflow:hidden}
.signup-form .field{flex:1;background:var(--field);display:flex;align-items:center;gap:12px;padding-left:11px;color:var(--ink);font-size:13.5px}
.signup-form .send{width:87px;background:var(--send);display:flex;align-items:center;justify-content:center;font-size:14px;color:var(--white)}

/* laptop */
.laptop{position:absolute;left:565px;top:168px}
.lid{position:absolute;left:0;top:0;width:483px;height:328px;background:var(--bezel);border-radius:14px 14px 0 0;border:2px solid #3a3d44}
.screen{position:absolute;left:16px;top:22px;width:447px;height:279px;background:var(--panel);overflow:hidden}
.lid-label{position:absolute;left:0;right:0;bottom:5px;text-align:center;font-size:7px;color:#c9ccd3}
.base{position:absolute;left:-53px;top:327px;width:590px;height:8px;background:linear-gradient(#d9dbe0,var(--base) 60%,#7d8087);border-radius:0 0 60px 60px/0 0 8px 8px}
.base-notch{position:absolute;left:238px;top:0;width:112px;height:3px;background:#9ea1a8;border-radius:0 0 4px 4px}
.shadow{position:absolute;left:-10px;top:336px;width:500px;height:14px;border-radius:50%;background:rgba(0,20,60,.25);filter:blur(6px)}

/* dashboard */
.side{position:absolute;left:0;top:0;width:82px;height:279px;background:linear-gradient(var(--side-top),var(--side-bottom));color:var(--white)}
.side-brand{position:absolute;left:9px;top:7px;display:flex;gap:4px;align-items:center;font-size:5px;font-weight:600;line-height:5.5px}
.side-brand i{display:block;width:10px;height:10px;border-radius:50%;background:var(--white)}
.menu{position:absolute;left:10px;top:40px;width:64px;list-style:none;font-size:4px;line-height:15px;letter-spacing:.2px}
.menu li{display:flex;align-items:center;gap:6px;height:15px}
.menu .sub{padding-left:10px;color:#bfe2f6}
.menu .ico{width:4px;height:4px;background:var(--white);border-radius:1px}
.menu .badge{width:5px;height:5px;border-radius:50%;background:#f2a33a;margin-left:auto}
.menu .gap{height:55px}
.user-box{position:absolute;left:10px;top:122px;width:63px;height:40px;background:rgba(255,255,255,.14);border-radius:2px;font-size:3.5px;line-height:4.5px;padding:5px}
.user-box .who{display:flex;gap:4px;align-items:center;font-weight:600;font-size:4px;line-height:4.5px}
.user-box .who i{width:9px;height:9px;border-radius:50%;background:#c99c7f}
.user-box .who small{font-weight:400;font-size:3px}
.user-box p{margin-top:7px}
.side-tools{position:absolute;left:10px;top:256px;display:flex;gap:3px}
.side-tools span{width:30px;height:15px;background:rgba(255,255,255,.14);display:flex;align-items:center;justify-content:center}
.side-tools span i{width:4px;height:4px;border:1px solid var(--white);border-radius:50%}

.topbar .cta{position:absolute;left:96px;top:7px;width:84px;height:11px;border-radius:6px;background:var(--side-top);font-size:3.6px;color:var(--white);display:flex;align-items:center;justify-content:center}
.topbar .add{position:absolute;left:186px;top:8px;width:10px;height:10px;border-radius:50%;background:#3b7bde;color:var(--white);font-size:8px;line-height:9px;text-align:center}
.topbar .search{position:absolute;left:328px;top:7px;width:63px;height:11px;border-radius:6px;background:var(--white);font-size:3.5px;color:#aab;padding:3px 9px}
.topbar .me{position:absolute;left:400px;top:7px;display:flex;gap:4px;align-items:center;font-size:4px;color:var(--accent)}
.topbar .me i{width:10px;height:10px;border-radius:50%;background:#c98e6b}
.filters{position:absolute;left:98px;top:24px;display:flex;gap:4px}
.filters span{height:11px;background:var(--white);font-size:3.8px;color:var(--accent);padding:3px 4px;display:flex;justify-content:space-between}
.filters span::after{content:"▾";color:#999}
.dropdown{position:absolute;left:171px;top:35px;width:61px;height:40px;background:var(--white);box-shadow:0 1px 3px rgba(0,0,0,.15);font-size:3.8px;color:var(--muted);padding:3px 5px;line-height:11px}

.card{position:absolute;width:99px;height:112px;background:var(--card);color:var(--ink);text-align:center}
.card .tags{position:absolute;top:5px;left:10px;right:10px;display:flex;justify-content:space-between;font-size:3.5px}
.card .tags span::before{content:"";display:inline-block;width:3px;height:3px;border-radius:50%;background:#3b7bde;margin-right:3px;vertical-align:middle}
.card .tags span:last-child::before{background:#222}
.card .poster{position:absolute;top:16px;left:10px;right:6px;display:flex;gap:5px;align-items:center;text-align:left}
.card .avatar{flex:none;width:15px;height:15px;border-radius:50%;background:#c79a7e}
.card .name{font-size:4.6px;font-weight:600;text-transform:uppercase;line-height:6px}
.card .role{font-size:2.8px;line-height:3.5px;color:var(--muted);white-space:nowrap}
.card .stars{position:absolute;top:35px;left:0;right:0;font-size:4.5px;line-height:6px;color:var(--star);letter-spacing:.5px}
.card .title{position:absolute;top:41px;left:0;right:0;font-size:8.4px;line-height:10px;font-weight:700;color:var(--accent);text-transform:uppercase;letter-spacing:-.1px;white-space:nowrap}
.card .date{position:absolute;top:51px;left:0;right:0;font-size:3px;line-height:4px;color:var(--muted)}
.card .desc{position:absolute;top:57px;left:18px;right:18px;font-size:3px;line-height:4.6px;color:#9aa0b0}
.card .stats{position:absolute;top:86px;left:6px;right:6px;display:flex;justify-content:space-around}
.card .stats div{display:flex;flex-direction:column;align-items:center;font-size:7px;color:var(--accent);line-height:7px}
.card .stats i{width:4px;height:4px;border-radius:50%;background:#3b7bde;margin-bottom:2px}
.card .stats small{font-size:2.6px;color:var(--muted);line-height:4px}
.card .ribbon{position:absolute;left:-1px;top:0;width:5px;height:18px}
.ribbon.red{background:var(--tag-red);left:3px;height:14px}
.ribbon.pink{background:var(--tag-pink);height:26px}
.scroll{position:absolute;left:437px;top:84px;width:1.5px;height:70px;background:#c7ccd6}
</style>
</head>
<body>
<main class="canvas">
  <svg class="backdrop" width="1200" height="675" viewBox="0 0 1200 675" aria-hidden="true">
    <polygon points="1124,0 1200,0 1200,675 452,675" fill="var(--blue)"/>
  </svg>

  <header>
    <div class="brand"><span class="brand-dot"></span><span class="brand-name">CRUX<br>FINDER</span></div>
    <nav class="nav"><a class="login" href="#">LOG IN</a><a class="signup" href="#">SIGN UP</a></nav>
  </header>

  <h1 class="hero-title">INTRODUCING <strong>CRUX FINDER</strong></h1>
  <p class="hero-copy">Lorem ipsum dolor sit amet, consectetur adipiscing elit. Aenean<br>sed diam volutpat, consequat purus sed, interdum nibh. Integer ultriciesfe<br>diam ac vulputate. Aenean finibus ac enim a porta. Quisque volutpat efficitur<br>fringilla. Quisque sit amet accumsan nisl.</p>

  <form class="signup-form">
    <div class="field">
      <svg width="20" height="16" viewBox="0 0 20 16" aria-hidden="true"><path d="M0 7 L20 0 L14 16 L9 10 Z" fill="var(--blue)"/><path d="M9 10 L20 0" stroke="var(--field)" stroke-width="1"/></svg>
      Email Address
    </div>
    <div class="send">Send</div>
  </form>

  <section class="laptop" aria-label="Problem search dashboard preview">
    <div class="shadow"></div>
    <div class="lid">
      <div class="screen">
        <aside class="side">
          <div class="side-brand"><i></i><span>SHAKE<br>YOUR TRADE</span></div>
          <ul class="menu">
            <li><span class="ico"></span>PROBLEMS</li>
            <li class="sub">LATEST</li>
            <li class="sub">TRENDING</li>
            <li class="sub">TOP RATED</li>
            <li><span class="ico"></span>NEWS</li>
            <li class="gap"></li>
            <li><span class="ico"></span>MESSAGES<span class="badge"></span></li>
            <li><span class="ico"></span>NOTIFICATIONS<span class="badge"></span></li>
            <li><span class="ico"></span>PROFILE</li>
            <li><span class="ico"></span>TEAM PROFILE</li>
          </ul>
          <div class="user-box">
            <div class="who"><i role="img" aria-label="Member avatar"></i><span>JON DALE<br><small>team member</small></span></div>
            <p>A new study was posted. Find out about it.</p>
          </div>
          <div class="side-tools"><span><i></i></span><span><i></i></span></div>
        </aside>

        <div class="topbar">
          <span class="cta">SOLVE OUR PROBLEM</span>
          <span class="add">+</span>
          <span class="search">Search</span>
          <span class="me"><i role="img" aria-label="User avatar"></i>Jon</span>
        </div>
        <div class="filters">
          <span style="width:51px">Chemical</span>
          <span style="width:58px">Stage</span>
          <span style="width:51px">Filter</span>
          <span style="width:51px">Filter</span>
          <span style="width:51px">Date</span>
          <span style="width:46px">Rating</span>
        </div>

        <article class="card" style="left:98px;top:40px">
          <div class="tags"><span>Chemical</span><span>Team Started</span></div>
          <div class="poster"><i class="avatar" role="img" aria-label="Poster photo"></i><div><div class="name">Matteo</div><div class="role">Current Position</div></div></div>
          <div class="stars">★★★★★</div><div class="title">Cure Cancer</div><div class="date">Start date: 20/09/2016</div>
          <p class="desc">Short note on the problem space and who it hurts most today in the lab.</p>
          <div class="stats"><div><i></i>1061<small>Following</small></div><div><i></i>983<small>Teams</small></div><div><i></i>4190<small>Discussions</small></div></div>
        </article>
        <div class="dropdown">Just Started<br>Team Formed<br>Business Formed</div>

        <article class="card" style="left:213px;top:40px">
          <span class="ribbon red"></span>
          <div class="tags"><span>Chemical</span><span>Team Started</span></div>
          <div class="poster"><i class="avatar" role="img" aria-label="Poster photo"></i><div><div class="name">Phil Jonas</div><div class="role">Current Position: Chief Scientist at N.I.T</div></div></div>
          <div class="stars">★★★★★</div><div class="title">Cure Ebola</div><div class="date">Start date: 13/03/2016</div>
          <p class="desc">Short note on the problem space and who it hurts most today in the field.</p>
          <div class="stats"><div><i></i>53<small>Following</small></div><div><i></i>18<small>Teams</small></div><div><i></i>352<small>Discussions</small></div></div>
        </article>

        <article class="card" style="left:329px;top:40px">
          <div class="tags"><span>Chemical</span><span>Team Started</span></div>
          <div class="poster"><i class="avatar" role="img" aria-label="Poster photo"></i><div><div class="name">James Dorn</div><div class="role">Current Position: Scientist at N.I.T</div></div></div>
          <div class="stars">★★★☆☆</div><div class="title">Thyroid Problem</div><div class="date">Start date: 01/08/2016</div>
          <p class="desc">Short note on the problem space and who it hurts most today in clinics.</p>
          <div class="stats"><div><i></i>73<small>Following</small></div><div><i></i>24<small>Teams</small></div><div><i></i>542<small>Discussions</small></div></div>
        </article>

        <article class="card" style="left:98px;top:158px">
          <span class="ribbon pink"></span>
          <div class="tags"><span>Chemical</span><span>Team Started</span></div>
          <div class="poster"><i class="avatar" role="img" aria-label="Poster photo"></i><div><div class="name">Lily Stanway</div><div class="role">Current Position: Chief Surgeon at KRL</div></div></div>
          <div class="stars">★★★★☆</div><div class="title">Heart Surgery</div><div class="date">Start date: 31/12/2016</div>
          <p class="desc">Short note on the problem space and who it hurts most today in surgery.</p>
          <div class="stats"><div><i></i>159<small>Following</small></div><div><i></i>90<small>Teams</small></div><div><i></i>786<small>Discussions</small></div></div>
        </article>

        <article class="card" style="left:213px;top:158px">
          <div class="tags"><span>Chemical</span><span>Team Started</span></div>
          <div class="poster"><i class="avatar" role="img" aria-label="Poster photo"></i><div><div class="name">Dave Obrand</div><div class="role">Current Position: Researcher at Quillmoor Labs</div></div></div>
          <div class="stars">★★☆☆☆</div><div class="title">Fever Discovery</div><div class="date">Start date: 10/12/2016</div>
          <p class="desc">Short note on the problem space and who it hurts most today at home.</p>
          <div class="stats"><div><i></i>02<small>Following</small></div><div><i></i>01<small>Teams</small></div><div><i></i>07<small>Discussions</small></div></div>
        </article>

        <article class="card" style="left:329px;top:158px">
          <div class="tags"><span>Chemical</span><span>Team Started</span></div>
          <div class="poster"><i class="avatar" role="img" aria-label="Poster photo"></i><div><div class="name">Tilly Marsh</div><div class="role">Current Position: Scientist at Hartwell</div></div></div>
          <div class="stars">★★★☆☆</div><div class="title">Fever Revolution</div><div class="date">Start date: 29/03/2016</div>
          <p class="desc">Short note on the problem space and who it hurts most today in wards.</p>
          <div class="stats"><div><i></i>12<small>Following</small></div><div><i></i>06<small>Teams</small></div><div><i></i>29<small>Discussions</small></div></div>
        </article>
        <span class="scroll"></span>
      </div>
      <div class="lid-label">Lumabook</div>
    </div>
    <div class="base"><span class="base-notch"></span></div>
  </section>
</main>
</body>
</html>
```